Business Card (I don't have a logo)

I'm bootstrapping a new venture and need a business card and "look" for it. I'd like to print one side only, but could do a bleed to the edges, but don't need to. See my website: www.calebharrowpartners.example to get a sense of the photos that relate to the look/feel of my company.

Target Market(s)

high tech start-up company CEO's in Silicon Valley

Industry/Entity Type

Business

Requirements
Must have
• a look that can cut/paste onto my website that integrates easily with the front page photo. see www.calebharrowpartners.example

```html
<!DOCTYPE html>
<html lang="en">
<head>
<meta charset="utf-8">
<title>Caleb Harrow Partners – Business Cards</title>
<link href="https://fonts.googleapis.com/css2?family=Maven+Pro:wght@400;500;600&display=swap" rel="stylesheet">
<style>
  :root {
    --backdrop: #e9e7e3;
    --card-white: #ffffff;
    --ink: #111111;
    --ink-soft: #555555;
    --band-dark: #0b0b0b;
    --band-mid: #2a2a2a;
    --sky: #cfe3f3;
    --sky-deep: #b6d3ec;
    --icon-blue: #1f8fc8;
    --rule-grey: #9a9a9a;
  }
  * { box-sizing: border-box; margin: 0; padding: 0; }
  html, body { width: 1200px; height: 900px; overflow: hidden; }
  body {
    background: var(--backdrop);
    font-family: "Maven Pro", sans-serif;
    color: var(--ink);
    position: relative;
  }
  .card {
    position: absolute;
    background: var(--card-white);
    border-radius: 22px;
    overflow: hidden;
    box-shadow: 0 6px 16px rgba(0,0,0,0.25);
  }
  .brand { font-size: 27px; font-weight: 400; white-space: nowrap; }
  .brand strong { font-weight: 600; }
  .rule-black { position: absolute; left: 0; right: 0; height: 5px; background: var(--band-dark); }
  .rule-grey { position: absolute; left: 0; right: 0; height: 2px; background: var(--rule-grey); }
  .person-name { font-size: 21px; font-weight: 600; }
  .person-role { font-size: 15px; color: var(--ink-soft); margin-top: 8px; }
  .contact-list { list-style: none; position: absolute; }
  .contact-list li {
    display: flex; align-items: center; gap: 10px;
    font-size: 17px; height: 30px; white-space: nowrap;
  }
  .contact-list .marker {
    width: 17px; height: 17px; border-radius: 3px;
    background: linear-gradient(var(--icon-blue), #1574a8);
    flex: none;
  }
  .footer-band {
    position: absolute; left: 0; right: 0; bottom: 0;
    background: linear-gradient(var(--band-mid), var(--band-dark));
    color: #fff;
    display: flex; align-items: center; justify-content: center;
    font-size: 17px;
  }

  /* landscape card */
  .card-landscape { left: 60px; top: 262px; width: 600px; height: 376px; }
  .card-landscape .header {
    position: absolute; left: 0; right: 0; top: 0; height: 60px;
    display: flex; align-items: center; justify-content: center;
  }
  .card-landscape .rule-black { top: 60px; }
  .card-landscape .rule-grey { top: 66px; }
  .card-landscape .body-panel {
    position: absolute; left: 0; right: 0; top: 68px; bottom: 43px;
    background: linear-gradient(var(--sky-deep), #eef5fb 22%, #ffffff 50%, #eef5fb 78%, var(--sky));
  }
  .card-landscape .identity {
    position: absolute; left: 0; width: 232px; top: 172px;
    text-align: center;
  }
  .card-landscape .divider {
    position: absolute; left: 232px; top: 120px; width: 2px; height: 180px;
    background: linear-gradient(transparent, #c6c9cc, transparent);
  }
  .card-landscape .contact-list { left: 255px; top: 154px; }
  .card-landscape .footer-band { height: 43px; }

  /* portrait card */
  .card-portrait { left: 745px; top: 165px; width: 381px; height: 595px; }
  .card-portrait .header {
    position: absolute; left: 0; right: 0; top: 0; height: 78px;
    display: flex; align-items: center; justify-content: center;
  }
  .card-portrait .rule-black { top: 78px; }
  .card-portrait .sky-band {
    position: absolute; left: 0; right: 0; top: 83px; height: 66px;
    background: linear-gradient(var(--sky-deep), #ffffff);
  }
  .card-portrait .identity { position: absolute; left: 0; right: 0; top: 166px; text-align: center; }
  .card-portrait .swoosh { position: absolute; left: 45px; top: 226px; }
  .card-portrait .address {
    position: absolute; left: 0; right: 0; top: 282px;
    text-align: center; font-size: 19px; line-height: 30px;
  }
  .card-portrait .contact-list { left: 32px; top: 389px; }
  .card-portrait .footer-band { height: 45px; }
</style>
</head>
<body>

<section class="card card-landscape" aria-label="Landscape business card">
  <header class="header"><div class="brand"><strong>Caleb Harrow</strong> Partners</div></header>
  <div class="rule-black"></div>
  <div class="rule-grey"></div>
  <div class="body-panel"></div>
  <div class="identity">
    <div class="person-name">Caleb Harrow</div>
    <div class="person-role">Divisional CEO</div>
  </div>
  <div class="divider"></div>
  <ul class="contact-list">
    <li><span class="marker"></span>0043 1 5550000-00</li>
    <li><span class="marker"></span>0043 1 5550000-00</li>
    <li><span class="marker"></span>info@calebharrowpartners.example</li>
    <li><span class="marker"></span>www.calebharrowpartners.example</li>
  </ul>
  <footer class="footer-band">41 Alder Lane Brook Hollow New York, USA</footer>
</section>

<section class="card card-portrait" aria-label="Portrait business card">
  <header class="header"><div class="brand"><strong>Caleb Harrow</strong> Partners</div></header>
  <div class="rule-black"></div>
  <div class="sky-band"></div>
  <div class="identity">
    <div class="person-name">Caleb Harrow</div>
    <div class="person-role">Divisional CEO</div>
  </div>
  <svg class="swoosh" width="290" height="12" viewBox="0 0 290 12" aria-hidden="true">
    <defs>
      <linearGradient id="swoosh-fade" x1="0" x2="1">
        <stop offset="0" stop-color="#999" stop-opacity="0"/>
        <stop offset="0.5" stop-color="#888" stop-opacity="0.8"/>
        <stop offset="1" stop-color="#999" stop-opacity="0"/>
      </linearGradient>
    </defs>
    <path d="M0 8 Q145 0 290 4 Q145 5 0 8 Z" fill="url(#swoosh-fade)"/>
  </svg>
  <div class="address">41 Alder Lane Brook Hollow<br>New York, USA</div>
  <ul class="contact-list">
    <li><span class="marker"></span>0043 1 5550000-00</li>
    <li><span class="marker"></span>0043 1 5550000-00</li>
    <li><span class="marker"></span>info@calebharrowpartners.example</li>
    <li><span class="marker"></span>www.calebharrowpartners.example</li>
  </ul>
  <footer class="footer-band"></footer>
</section>

</body>
</html>
```